Winelabel for Italian Wine incl. box.

Front and back label for new Italian wine.
It´s a premium redwine,
Size of Labels: Front 100x115 | Back 60x85
For front label we can also use these sizes:
95X115 - 100x100 – 86x97 – 100x110
For back labels : 60X90 – 60X95 – 60X100
We can only use one type of foil finishing.
BRAND = FIORALBA dal` Colle Brisco (in 2 lines)
2. titel = Calice di Sera
Semi lines = Ancient vinification Traditions | Truscany
Style = elegant Italian coloured Harlequin,
Other colors using white/black/gold
Include a round "water-mark" with text : Selected for loyal winelowers
Back label will be short story + legal data + barcode.
Outer box of 6 bottles case design print on all 4 fronts.

```html
<!DOCTYPE html>
<html lang="it">
<head>
<meta charset="utf-8">
<title>Fioralba dal' Colle Brisco – Front Label</title>
<link href="https://fonts.googleapis.com/css2?family=Cinzel:wght@400;500&family=Pinyon+Script&family=Montserrat:wght@400&family=Playfair+Display:wght@400&display=swap" rel="stylesheet">
<style>
  :root {
    --backdrop: #f2f6f7;
    --paper: #f8f8f6;
    --ink: #121212;
    --gold: #c9a53e;
    --gold-light: #f2e7a2;
    --gold-mid: #dcc36a;
    --gold-deep: #b58e2c;
  }
  html, body {
    margin: 0;
    padding: 0;
    width: 900px;
    height: 1200px;
    overflow: hidden;
    background: var(--backdrop);
  }
  .canvas {
    position: relative;
    width: 900px;
    height: 1200px;
  }
  .front-label {
    position: absolute;
    left: 20px;
    top: 107px;
    width: 860px;
    height: 985px;
    background: var(--paper);
    box-shadow: 0 2px 10px rgba(0,0,0,0.08);
  }
  .gold-frame {
    position: absolute;
    left: 27px;
    top: 27px;
    right: 27px;
    bottom: 27px;
    border: 5px solid var(--gold);
    box-sizing: border-box;
  }
  .foil-block {
    position: absolute;
    left: 170px;
    top: 0;
    width: 519px;
    height: 317px;
    background: linear-gradient(135deg, var(--gold-light) 0%, var(--gold-mid) 45%, var(--gold) 75%, var(--gold-mid) 100%);
    text-align: center;
  }
  .brand-name {
    position: absolute;
    left: 0;
    right: 0;
    top: 128px;
    margin: 0;
    font-family: "Cinzel", "Playfair Display", serif;
    font-weight: 400;
    font-size: 74px;
    line-height: 1;
    color: var(--ink);
    letter-spacing: -1px;
  }
  .brand-sub {
    position: absolute;
    left: 0;
    right: 0;
    top: 222px;
    margin: 0;
    font-family: "Playfair Display", serif;
    font-size: 31px;
    line-height: 1;
    color: var(--ink);
    letter-spacing: 1px;
    text-transform: uppercase;
  }
  .wine-title {
    position: absolute;
    left: 0;
    right: 0;
    top: 438px;
    margin: 0;
    text-align: center;
    font-family: "Pinyon Script", cursive;
    font-weight: 400;
    font-size: 76px;
    line-height: 1;
    color: var(--gold-mid);
  }
  .tagline {
    position: absolute;
    left: 0;
    right: 0;
    top: 606px;
    margin: 0;
    text-align: center;
    font-family: "Montserrat", sans-serif;
    font-size: 25px;
    line-height: 1;
    color: var(--ink);
    letter-spacing: 0.5px;
  }
  .region {
    position: absolute;
    left: 0;
    right: 0;
    top: 640px;
    margin: 0;
    text-align: center;
    font-family: "Pinyon Script", cursive;
    font-size: 72px;
    line-height: 1;
    color: var(--ink);
  }
  .loyalty-seal {
    position: absolute;
    left: 338px;
    top: 748px;
    width: 168px;
    height: 168px;
  }
</style>
</head>
<body>
<main class="canvas">
  <section class="front-label">
    <div class="gold-frame"></div>
    <header class="foil-block">
      <h1 class="brand-name">FIORALBA</h1>
      <p class="brand-sub">dal' Colle Brisco</p>
    </header>
    <h2 class="wine-title">Calice di Sera</h2>
    <p class="tagline">ANCIENT VINIFICATION TRADITIONS</p>
    <p class="region">Truscany</p>
    <svg class="loyalty-seal" viewBox="0 0 168 168" role="img" aria-label="Gold seal for loyal wine lovers">
      <defs>
        <radialGradient id="sealGold" cx="40%" cy="35%" r="70%">
          <stop offset="0%" stop-color="#f4e49a"/>
          <stop offset="60%" stop-color="#d9b648"/>
          <stop offset="100%" stop-color="#b58e2c"/>
        </radialGradient>
      </defs>
      <circle cx="84" cy="84" r="82" fill="url(#sealGold)"/>
      <circle cx="84" cy="84" r="70" fill="none" stroke="#b58e2c" stroke-width="2"/>
    </svg>
  </section>
</main>
</body>
</html>
```